Marrow Creek Outdoors League needs a poster for fish fry

We need a flyer made for a fish fry. Things we need on it;

Date: Sunday, February 12th
Location: Brennock Sportsdome Hall
Time: 5-6:30 pm
Cost: $15 for adults, $10 for 12 & under, free for preschool

Requirements
Must have
• Must have our logo on it.

```html
<!DOCTYPE html>
<html lang="en">
<head>
<meta charset="utf-8">
<title>Fish Fry – Marrow Creek Outdoors League</title>
<link rel="stylesheet" href="https://fonts.googleapis.com/css2?family=Oswald:wght@500;600&family=Courgette&family=Playfair+Display:wght@700&family=Montserrat:wght@400&display=swap">
<style>
  :root {
    --backdrop: #2f2f2f;
    --mustard: #d8b53a;
    --mustard-deep: #b8952a;
    --ink: #1d1914;
    --night: #171512;
    --gold: #f3d334;
    --white: #ffffff;
  }
  * { margin: 0; padding: 0; box-sizing: border-box; }
  html, body { width: 991px; height: 1200px; overflow: hidden; }
  body { background: var(--backdrop); position: relative; }

  .poster {
    position: absolute; left: 67px; top: 0;
    width: 857px; height: 1200px; overflow: hidden;
    background: radial-gradient(ellipse at 45% 30%, #e4c44a 0%, var(--mustard) 55%, var(--mustard-deep) 100%);
  }
  .night-band {
    position: absolute; left: 0; top: 713px; width: 100%; height: 487px;
    background: var(--night);
  }
  .headline {
    position: absolute; left: 28px; top: 44px;
    font: 600 150px/1 "Oswald", sans-serif; letter-spacing: 2px;
    color: var(--ink); text-transform: uppercase; white-space: nowrap;
  }
  .quality-badge {
    position: absolute; left: 621px; top: 44px; width: 180px; height: 172px;
    border: 5px solid var(--ink); border-radius: 50%;
  }
  .event-date { position: absolute; left: 0; top: 230px; width: 420px; height: 110px; color: var(--ink); }
  .event-date .weekday-month {
    position: absolute; right: 185px; top: 4px; text-align: right;
    font: 500 44px/1.1 "Oswald", sans-serif; text-transform: uppercase;
  }
  .event-date .day {
    position: absolute; left: 244px; top: -10px;
    font: 600 120px/1 "Oswald", sans-serif; letter-spacing: -4px;
  }
  .event-date .suffix {
    position: absolute; left: 352px; top: 18px;
    font: 500 44px/1 "Oswald", sans-serif;
  }
  .date-rule {
    position: absolute; left: 161px; top: 357px; width: 135px; height: 4px;
    background: var(--ink); border-radius: 2px;
  }
  .event-time {
    position: absolute; left: 103px; top: 392px;
    font: 400 34px/1 "Courgette", cursive; color: var(--ink); white-space: nowrap;
  }
  .fish-mark {
    position: absolute; left: 57px; top: 482px; width: 188px; height: 90px;
    background: linear-gradient(90deg, #2a231a, #3b311f); border-radius: 50% 40% 40% 50%;
  }
  .hero-dish { position: absolute; left: 0; top: 0; width: 857px; height: 800px; }
  .side-dish {
    position: absolute; left: 42px; top: 612px; width: 300px; height: 216px; border-radius: 50%;
    background: radial-gradient(ellipse at 50% 50%, #b06a45 0%, #d9b25a 40%, #f6f6f4 72%, #e8e8e6 100%);
    box-shadow: 0 0 0 4px var(--gold);
  }
  .cost-box {
    position: absolute; left: 59px; top: 918px; width: 451px; height: 233px;
    border: 2px solid var(--gold);
  }
  .box-title {
    position: absolute; left: 50%; top: -26px; transform: translateX(-50%);
    padding: 0 12px; background: var(--night); color: var(--gold);
    font: 700 44px/1 "Playfair Display", serif; white-space: nowrap;
  }
  .price {
    position: absolute; top: 52px; color: var(--gold); white-space: nowrap;
    font-variant-numeric: lining-nums;
  }
  .price .amount { font: 700 54px/1 "Playfair Display", serif; font-variant-numeric: lining-nums; }
  .price .label { font: 700 17px/1 "Playfair Display", serif; margin-left: 4px; font-variant-numeric: lining-nums; }
  .price.adult { left: 28px; }
  .price.child { left: 216px; }
  .free-line {
    position: absolute; left: 80px; top: 158px; width: 290px; height: 44px;
    border-top: 2px dotted var(--gold); border-bottom: 2px dotted var(--gold);
    display: flex; align-items: center; justify-content: center; white-space: nowrap;
    color: var(--white); font: 700 18px/1 "Playfair Display", serif;
  }
  .host { position: absolute; left: 600px; top: 880px; width: 180px; text-align: center; }
  .host-mark {
    width: 62px; height: 62px; margin: 0 auto 14px;
    border-radius: 50%; background: var(--white);
  }
  .host-name {
    color: var(--white); font: 700 20px/1.2 "Playfair Display", serif;
  }
  .location-box {
    position: absolute; left: 575px; top: 1068px; width: 226px; height: 83px;
    border: 2px solid var(--gold);
  }
  .location-box .box-title { font-size: 22px; top: -14px; padding: 0 6px; }
  .location-box address {
    position: absolute; left: 0; top: 22px; width: 100%; text-align: center;
    font: 400 16px/1.4 "Montserrat", sans-serif; font-style: normal;
    letter-spacing: 1.5px; color: var(--white); white-space: nowrap;
  }
</style>
</head>
<body>
  <main class="poster">
    <div class="night-band"></div>

    <svg class="hero-dish" viewBox="0 0 857 800" role="img" aria-label="Whole fried fish on a white platter with lettuce, lemon, tomato, olives and a dip">
      <defs>
        <radialGradient id="platter-fill" cx="0.55" cy="0.5" r="0.6">
          <stop offset="0" stop-color="#b0602e"/>
          <stop offset="0.4" stop-color="#8fb54a"/>
          <stop offset="0.72" stop-color="#f4f4f2"/>
          <stop offset="1" stop-color="#e6e6e3"/>
        </radialGradient>
      </defs>
      <polygon points="524,276 815,334 705,748 255,578" fill="url(#platter-fill)" stroke="#eeeeec" stroke-width="14" stroke-linejoin="round"/>
    </svg>

    <h1 class="headline">Fish Fry</h1>
    <div class="quality-badge" aria-hidden="true"></div>

    <div class="event-date">
      <div class="weekday-month">Sunday<br>February</div>
      <div class="day">12</div>
      <div class="suffix">TH</div>
    </div>
    <div class="date-rule"></div>
    <p class="event-time">Time: 5-6:30 pm</p>

    <div class="fish-mark" role="img" aria-label="Silhouette of a fish"></div>
    <div class="side-dish" role="img" aria-label="Fried fish plate with fries, onion rings and salad"></div>

    <section class="cost-box">
      <h2 class="box-title">COST</h2>
      <div class="price adult"><span class="amount">$15</span><span class="label">for Adults</span></div>
      <div class="price child"><span class="amount">$10</span><span class="label">for 12 &amp; under</span></div>
      <div class="free-line">FREE FOR PRESCHOOL</div>
    </section>

    <div class="host">
      <div class="host-mark" aria-hidden="true"></div>
      <div class="host-name">Marrow Creek<br>Outdoors League</div>
    </div>

    <section class="location-box">
      <h2 class="box-title">LOCATION</h2>
      <address>Brennock Sportsdome<br>Hall</address>
    </section>
  </main>
</body>
</html>
```